Lorvex CBD oil tincture bottle product label design

I need a product label designed for a CBD hemp oil tincture bottle. The label size should be 34mm x 62mm narrow edge leading. Format wise, a high quality jpeg or pdf.

The product is a food supplement for health benefits. The colour scheme is green/gold. The logo and all of the information on the attached label needs to be included however the image, and design/layout can be changed. I do like the label that's attached Id just like others to compare.

Target Market(s)

health/supplement market

Requirements
Must have
• Green/gold theme

```html
<!DOCTYPE html>
<html lang="en">
<head>
<meta charset="utf-8">
<title>Lorvex Hemp Oil 5% CBD – Bottle Label</title>
<link rel="stylesheet" href="https://fonts.googleapis.com/css2?family=Ultra&family=Roboto+Condensed:wght@400;700&family=Open+Sans:wght@300&display=swap">
<style>
  :root {
    --bg: #2a2a2c;
    --label-green: #1c3a20;
    --panel-border: #1f9a4a;
    --panel-fill: #f4f5f7;
    --ink: #1b261d;
    --gold: #f4ec2a;
    --white: #ffffff;
    --figure-light: #2f7a45;
    --figure-dark: #0f2a16;
  }
  * { box-sizing: border-box; margin: 0; padding: 0; }
  html, body { width: 1200px; height: 738px; overflow: hidden; background: var(--bg); }
  .canvas { position: relative; width: 1200px; height: 738px; }

  .label {
    position: absolute; left: 81px; top: 85px; width: 1038px; height: 567px;
    background: var(--label-green);
  }

  .figure-art {
    position: absolute; left: 305px; top: 67px; width: 422px; height: 418px;
    background: radial-gradient(ellipse 45% 60% at 50% 40%, var(--figure-light) 0%, #1d4d2b 45%, var(--figure-dark) 100%);
  }

  .top-tab { position: absolute; left: 311px; top: 0; width: 414px; height: 78px; }
  .top-tab svg, .bottom-tab svg { position: absolute; inset: 0; }
  .top-tab span, .bottom-tab span {
    position: relative; display: block; text-align: center;
    font-family: "Ultra", serif; color: var(--ink);
  }
  .top-tab span { font-size: 27px; line-height: 78px; padding-top: 8px; }

  .logo-slot {
    position: absolute; left: 305px; width: 422px; top: 216px; text-align: center;
    font-family: "Open Sans", sans-serif; font-weight: 300; font-size: 32px; color: var(--white);
  }

  .product-name {
    position: absolute; left: 305px; width: 422px; top: 335px; text-align: center;
    font-family: "Ultra", serif; color: var(--white); font-size: 64px; line-height: 62px;
  }
  .product-name .strength { font-size: 68px; }

  .bottom-tab { position: absolute; left: 323px; top: 489px; width: 392px; height: 52px; }
  .bottom-tab span { font-size: 26px; line-height: 52px; }

  .info-panel {
    position: absolute; top: 36px; width: 283px; height: 509px;
    background: var(--panel-fill); border: 4px solid var(--panel-border); border-radius: 32px;
    font-family: "Roboto Condensed", sans-serif; color: var(--ink);
  }
  .info-panel--left { left: 21px; }
  .info-panel--right { left: 730px; }
  .info-panel > * { position: absolute; left: 16px; right: 4px; }
  .info-panel--right > * { left: 11px; right: 0; }

  .panel-heading { font-weight: 700; font-size: 22px; line-height: 26px; }
  .panel-body { font-size: 17px; line-height: 26.6px; letter-spacing: -0.3px; }
  .panel-lead { font-size: 22px; line-height: 28.5px; }
  .panel-lead strong { font-weight: 700; }
  .panel-rule { left: 10px !important; right: 26px !important; height: 2px; background: var(--ink); }
  .info-panel--right .panel-rule { left: 18px !important; right: 10px !important; }
</style>
</head>
<body>
<main class="canvas">
  <section class="label">
    <div class="figure-art" role="img" aria-label="Translucent green anatomical illustration of a human figure showing the skeleton and spine"></div>

    <div class="top-tab">
      <svg width="414" height="78" viewBox="0 0 414 78" aria-hidden="true">
        <path d="M0 0 H414 L378 50 Q360 78 320 78 H94 Q54 78 36 50 Z" fill="var(--gold)"/>
      </svg>
      <span>FULL SPECTRUM</span>
    </div>

    <div class="logo-slot">Logo Here</div>

    <h1 class="product-name">HEMP OIL<br><span class="strength">5% CBD</span></h1>

    <div class="bottom-tab">
      <svg width="392" height="52" viewBox="0 0 392 52" aria-hidden="true">
        <path d="M26 0 H392 L376 30 Q366 52 340 52 H0 L14 22 Q22 0 26 0 Z" fill="var(--white)"/>
      </svg>
      <span>CO2 EXTRACTED</span>
    </div>

    <aside class="info-panel info-panel--left">
      <h2 class="panel-heading" style="top:28px">CONTAINS:</h2>
      <p class="panel-body" style="top:79px">
        10ml organic certified hemp oil from<br>
        hemp (Cannabis Satiya).<br>
        Supercritical C02 extracted.<br>
        Hemp seed oil (77%),<br>
        hemp extract (23%).<br>
        500mg CBD+CBDa.<br>
        Approximately 2mg CBD per drop.
      </p>
      <p class="panel-lead" style="top:307px">Distributed by:<br><strong>LORVEX LTD</strong></p>
      <div class="panel-rule" style="top:394px"></div>
      <p class="panel-lead" style="top:405px"><strong>Manufactured in the UK</strong><br>10ml [033 oz]</p>
    </aside>

    <aside class="info-panel info-panel--right">
      <h2 class="panel-heading" style="top:28px">RECOMMENDED USE:</h2>
      <p class="panel-body" style="top:79px">
        As food supplement, use twice daily.<br>
        Place 10 – 15 drops under the tongue.<br>
        Hold for 60sec, then swallow.<br>
        Do not exceed 200mg/day.<br>
        Shake before use.
      </p>
      <p class="panel-lead" style="top:289px"><strong>STORAGE:</strong><br>Stre away from sunlight,<br>heat &amp; humidity.</p>
      <div class="panel-rule" style="top:394px"></div>
      <p class="panel-lead" style="top:405px">Batch:<br>User by:</p>
    </aside>
  </section>
</main>
</body>
</html>
```